New Business Card for Auto Repair and Performance Shop!

Need a redesign on a card that we have used for a while now. Something more update and modern, Serious but not too serious. Something confident, that shows the client that we are bespoke. Adding value.

Target Market(s)

Foreign Auto Repair and Performance

Industry/Entity Type

Automotive

Contact Information for Business Card

Utilize Logo, would like to change car silhouette to something Veltra,

Font styles to use
Sans Serif

Requirements
Must have
• business name, address, website, phone number.
MotoSerenix
4918 W. Birchwell Rd
Killeen, T.X. 76542
1-254-487-3106
www.moto-serenix-example.com

Specializing in Asian, European, and Domestic Auto Repair, Performance and Fabrication.

Clear space on back to for space to write appointment time and which client advisor helped the client.
Nice to have
• Up to the designers,

```html
<!DOCTYPE html>
<html lang="en">
<head>
<meta charset="utf-8">
<title>MotoSerenix Business Card</title>
<link rel="stylesheet" href="https://fonts.googleapis.com/css2?family=Montserrat:wght@400;500;600&display=swap">
<style>
  :root {
    --stage: #e6e8ea;
    --card-front: #d3d3d3;
    --card-back: #ffffff;
    --brand-red: #e8252a;
    --ink: #3a3a3a;
    --ink-soft: #555555;
    --edge-shadow: rgba(0,0,0,0.18);
  }
  * { margin: 0; padding: 0; box-sizing: border-box; }
  html, body { width: 1200px; height: 913px; overflow: hidden; }
  body {
    background: var(--stage);
    font-family: "Montserrat", sans-serif;
    position: relative;
  }
  .card {
    position: absolute;
    width: 560px;
    height: 320px;
    box-shadow: 0 6px 18px var(--edge-shadow);
    overflow: hidden;
  }
  .card--front { left: 50px; top: 80px; background: var(--card-front); }
  .card--back { left: 590px; top: 510px; background: var(--card-back); }

  .front__name {
    position: absolute;
    left: 0; right: 0; top: 128px;
    text-align: center;
    color: var(--brand-red);
    font-weight: 600;
    font-size: 38px;
    letter-spacing: 0.32em;
    padding-left: 0.32em;
  }
  .front__tagline {
    position: absolute;
    left: 0; right: 0; bottom: 52px;
    text-align: center;
    color: var(--ink-soft);
    font-weight: 500;
    font-size: 12.5px;
    letter-spacing: 0.08em;
    line-height: 1.35;
    text-transform: uppercase;
  }

  .back__edge {
    position: absolute;
    left: 0; top: 196px;
    width: 8px; height: 60px;
    background: var(--brand-red);
  }
  .back__details {
    position: absolute;
    left: 40px; bottom: 34px;
    color: var(--ink);
    text-transform: uppercase;
  }
  .back__name {
    color: var(--brand-red);
    font-weight: 600;
    font-size: 28px;
    letter-spacing: 0.12em;
    margin-bottom: 6px;
  }
  .back__address {
    font-size: 15px;
    line-height: 1.3;
    letter-spacing: 0.04em;
    margin-bottom: 8px;
  }
  .contact-line {
    display: flex;
    align-items: center;
    gap: 8px;
    font-size: 15px;
    letter-spacing: 0.04em;
    line-height: 1.4;
  }
  .contact-line svg { width: 14px; height: 14px; flex: none; }
</style>
</head>
<body>

<section class="card card--front" aria-label="Business card front">
  <div class="front__name">MOTOSERENIX</div>
  <p class="front__tagline">Specializing in Asian, European, and Domestic<br>Auto Repair, Performance and Fabrication</p>
</section>

<section class="card card--back" aria-label="Business card back">
  <div class="back__edge"></div>
  <div class="back__details">
    <div class="back__name">MOTOSERENIX</div>
    <p class="back__address">4918 W. Birchwell Rd<br>Killeen, T.X. 76542</p>
    <div class="contact-line">
      <svg viewBox="0 0 24 24" aria-hidden="true"><path fill="#e8252a" d="M6.6 10.8a15.1 15.1 0 0 0 6.6 6.6l2.2-2.2a1 1 0 0 1 1-.25 11.4 11.4 0 0 0 3.6.57 1 1 0 0 1 1 1V20a1 1 0 0 1-1 1A17 17 0 0 1 3 4a1 1 0 0 1 1-1h3.5a1 1 0 0 1 1 1c0 1.25.2 2.45.57 3.57a1 1 0 0 1-.25 1z"/></svg>
      <span>1-254-487-3106</span>
    </div>
    <div class="contact-line">
      <svg viewBox="0 0 24 24" aria-hidden="true"><circle cx="12" cy="12" r="9" fill="none" stroke="#e8252a" stroke-width="2.4"/><path d="M3 12h18M12 3c3 3 3 15 0 18M12 3c-3 3-3 15 0 18" fill="none" stroke="#e8252a" stroke-width="1.6"/></svg>
      <span>www.moto-serenix-example.com</span>
    </div>
  </div>
</section>

</body>
</html>
```